Etiketten-Design für Produkte eines Familienbetriebs mit Imkerei und Hühnerhaltung
Zielgruppe
Wir sind ein Familienbetrieb mit Imkerei und Hühnerhaltung. Wir suchen für unsere Produkte ein modernes Corporate Design, mit zentralen, bei jedem Produkt vorkommenden Elementen, sowie Elementen, welche produktindividuell sind.
Wir leben in einem 150 jährigen Riegelhaus, welches in der Umgebung sehr bekannt ist. Es soll im Etiketten-Design zentral erscheinen.
Unsere Produkte sind: Honig, Pollen, Eier
Aufgabenstellung
1. Zentrale, auf allen Etiketten wiederkehrende Elemente:
- Unser Riegelhaus (stilisiert) (Bild beiliegend)
- Das Wort 'Birkacher' (Anmerkung: ohne Anführungszeichen)
- die zentralen Elemente sollen die Produkte nicht überragen.
2. Dezente Adresse:
- Familie Dorlitz, Birkenau, CH-8765 Felsbach
3. Produkte:
a) Honig
Sorten: Waldhonig (dunkel), Blütenhonig (gelblich-goldig), Crèmehonig (gelblich-weisslich), Lavendelhonig (gelblich-goldig)
Die Honigsorten sollen farblich hervortreten.
Freifeld (zweizeilig): für die Lotnummer und die Haltbarkeitsangabe)
Gewicht: 250 g, 500 g
b) Pollen
Gewicht: 100 g
c) Eier
Verpackungseinheiten: 4er-, 6er-, 10er-Packung
Haltungsform: BIO-Haltung
das Wort 'frisch'
Farbe grün (=Bio) soll farblich hervortreten (ähnlich wie beim Honig)
Freifeld (zweizeilig: für das Eigewicht und die Haltbarkeitsangabe)
Bitte keine Stock-Bilder verwenden. Die Etiketten sollen schlicht, edel ,schörkellos und modern erscheinen.
Das Etikett soll Exklusivität und Qualität ausstrahlen. Etikettenhintergrund einfarbig.
Interessanterweise gibt es bei Weinen solche Etiketten. Ich habe einige rausgesucht und angehängt, um die Richtung vorzugeben. (Wein1-6)
Ich habe auch eine schlichte Honigetikette gefunden, die ins Schema passt. (Imker1)
Zusätzlich sind jetzt auch noch Farbbeispiele der Honigsorten zur besseren Abstimmung von Inhalt und Etikette beigelegt. Lavendelhonig ist dem Blütenhonig sehr ähnlich.
Etikettengrössen:
Honig/Pollen 250 g: 190 x 42 mm
Honig 500 g: 206 x 45 mm
Eier 4er: 60 x 60 mm
Eier 6er: 110 x 60 mm
Eier 10er: 170 x 60 cm

```html
<!DOCTYPE html>
<html lang="de">
<head>
<meta charset="utf-8">
<title>Blütenhonig – Etikette 250 g</title>
<link href="https://fonts.googleapis.com/css2?family=Cormorant+SC:wght@500;600&display=swap" rel="stylesheet">
<style>
  :root {
    --label-cream: #f6efdd;
    --honey-orange: #f2a221;
    --petal-light: #f6bf6a;
    --lot-yellow: #f7c51d;
    --lot-text: #fff8e6;
  }
  * { margin: 0; padding: 0; box-sizing: border-box; }
  html, body { width: 1200px; height: 265px; overflow: hidden; background: var(--label-cream); }
  .label {
    position: relative;
    width: 1200px;
    height: 265px;
    overflow: hidden;
    background: var(--label-cream);
    font-family: "Cormorant SC", "Times New Roman", serif;
    color: var(--honey-orange);
  }
  .blossom {
    position: absolute;
    width: 270px;
    height: 270px;
    border-radius: 50%;
    background: radial-gradient(circle, var(--petal-light) 0%, var(--petal-light) 38%, var(--honey-orange) 62%);
  }
  .blossom--left { left: -132px; top: -3px; }
  .blossom--right { right: -132px; top: -3px; }
  .variety {
    position: absolute;
    top: 18px;
    left: 0;
    width: 100%;
    text-align: center;
    font-size: 34px;
    font-weight: 600;
    letter-spacing: 1px;
  }
  .address {
    position: absolute;
    left: 244px;
    top: 92px;
    width: 200px;
    text-align: center;
    font-size: 19px;
    font-weight: 500;
    line-height: 27px;
  }
  .emblem {
    position: absolute;
    left: 0;
    top: 0;
  }
  .brand-name {
    position: absolute;
    top: 230px;
    left: 0;
    width: 100%;
    text-align: center;
    font-size: 20px;
    font-weight: 600;
    letter-spacing: 0.5px;
  }
  .weight {
    position: absolute;
    left: 762px;
    top: 112px;
    width: 120px;
    text-align: center;
    font-size: 36px;
    font-weight: 500;
  }
  .lot-field {
    position: absolute;
    left: 1017px;
    top: 140px;
    width: 160px;
    height: 104px;
    border-radius: 12px;
    background: var(--lot-yellow);
    color: var(--lot-text);
    padding: 13px 12px;
    font-size: 15px;
    font-weight: 500;
    line-height: 19px;
  }
</style>
</head>
<body>
  <div class="label">
    <div class="blossom blossom--left" role="img" aria-label="Stilisierte orange Blüte als Randdekor"></div>
    <div class="blossom blossom--right" role="img" aria-label="Stilisierte orange Blüte als Randdekor"></div>

    <h1 class="variety">Blütenhonig</h1>

    <p class="address">Familie Dorlitz<br>Birkenau<br>CH-8765 Felsbach</p>

    <svg class="emblem" width="1200" height="265" viewBox="0 0 1200 265">
      <circle cx="600" cy="152" r="80" fill="none" stroke="var(--honey-orange)" stroke-width="5"/>
      <circle cx="600" cy="146" r="52" fill="var(--petal-light)" opacity="0.45" role="img" aria-label="Stilisiertes Riegelhaus"/>
    </svg>
    <p class="brand-name">Birkacher</p>

    <p class="weight">250 g</p>

    <div class="lot-field">Lot-No.<br>123456789<br>Verbrauchen bis<br>TT.MM.JJ</div>
  </div>
</body>
</html>
```